Postcard Design

This is first time using your site I want to see samples Postcard for advertising roofing service. Looking for full color front and back.
We are a roofing co. in Hollywood ca. same location 90years. something with a good call to action. list company services ie.
Residential, commercial, repairs, new roofs, energy efficient, cool roofs Title 24, skylights. Licensed, insured bonded
Kestrelroofing.net
323-555-0174
I would like full address on back: Kestrel Roofing Co. Inc
2287 W. Tamsin Street
Hollywood, Ca 90038
3 Coupons: Free roof inspection, !0% off New roof installation call for details, Free gutter cleaning with any roof maintenance
Updates

Reason: only had 3 designers

Target Market(s)

home owners all age and income levels, higher end

Industry/Entity Type

Advertising

Requirements
Must have
• Coupons on back
Nice to have
• Looking for good mock roof advertising photos
Please use logos of roofing manufactures ie, Brackwold, LVR, Pellam Strude, Vantel Mark logos

```html
<!DOCTYPE html>
<html lang="en">
<head>
<meta charset="utf-8">
<title>Kestrel Roofing Co. Postcard</title>
<link href="https://fonts.googleapis.com/css2?family=Alice&family=Tinos:ital,wght@0,400;0,700;1,700&family=Teko:wght@600&display=swap" rel="stylesheet">
<style>
  :root{
    --stage:#414143;
    --blue:#0a6cb8;
    --blue-deep:#0b5a9c;
    --black:#0d0d0d;
    --white:#ffffff;
    --brown:#4a3027;
    --red:#e4202a;
    --green:#3fb24a;
    --ink:#1a1a1a;
  }
  *{margin:0;padding:0;box-sizing:border-box}
  html,body{width:1200px;height:1140px;overflow:hidden;background:var(--stage)}
  body{position:relative;font-family:"Tinos",serif;color:var(--white)}
  .card{position:absolute;background:var(--white);overflow:hidden;box-shadow:0 3px 8px rgba(0,0,0,.45)}
  .front{left:259px;top:44px;width:674px;height:505px}
  .back{left:260px;top:581px;width:672px;height:521px}

  .hero-photo{position:absolute;left:0;top:60px;width:674px;height:300px;
    background:linear-gradient(180deg,rgba(255,255,255,1) 0%,#dfe3e8 25%,#b9b3ab 55%,#8f7f70 100%)}
  .wave{position:absolute;left:0;top:0}
  .headline{position:absolute;left:277px;top:26px;font-family:"Alice",serif;font-size:22.5px;line-height:23px;color:var(--ink)}
  .brand{position:absolute;color:var(--brown);font-family:"Tinos",serif;font-weight:700;text-align:center}
  .front .brand{left:40px;top:58px;width:220px}
  .brand .name{font-size:25px;line-height:26px}
  .brand .tag{font-weight:400;font-size:10px;color:#333;margin-top:8px}
  .tag .sq{display:inline-block;width:6px;height:6px;background:var(--blue);margin:0 3px}
  .cta-label{position:absolute;left:38px;top:324px;font-family:"Alice",serif;font-size:26px;letter-spacing:.5px}
  .cta-phone{position:absolute;left:38px;top:348px;font-family:"Alice",serif;font-size:39px}
  .front .address{position:absolute;left:40px;top:400px;font-size:18px;line-height:21px;letter-spacing:.4px}
  .address b{font-weight:700}
  .credentials{position:absolute;left:306px;top:352px;list-style:none}
  .credentials li{display:flex;align-items:center;height:35px;font-family:"Teko",sans-serif;font-size:31px;letter-spacing:.5px}
  .credentials svg{margin-right:2px}
  .partners{position:absolute;left:460px;top:397px;width:198px;height:53px;background:var(--white);display:flex;justify-content:space-around;align-items:center}
  .partners span{width:30px;height:30px;display:block}
  .url-bar{position:absolute;left:0;top:468px;width:674px;height:37px;background:var(--black);text-align:center;font-size:19px;line-height:37px;letter-spacing:.5px}

  .about{position:absolute;left:0;top:0;width:325px;height:251px;background:var(--blue)}
  .intro{position:absolute;left:40px;top:42px;width:254px;font-size:14.5px;line-height:15px;text-align:justify;letter-spacing:.5px}
  .services-title{position:absolute;left:40px;top:101px;font-weight:700;font-size:16px;letter-spacing:1px}
  .sectors{position:absolute;left:40px;top:129px;font-weight:700;font-style:italic;font-size:16px;letter-spacing:1px}
  .services{position:absolute;left:40px;top:160px;list-style:none;font-size:15px;line-height:16.8px;letter-spacing:.4px}
  .services li{display:flex;align-items:center}
  .services svg{margin-right:3px}
  .offers{position:absolute;left:0;top:253px;width:325px;height:176px;background:var(--black)}
  .coupon{position:absolute;background:var(--white);border:2px dashed #222;outline:2px solid var(--white);color:var(--ink);text-align:center;font-weight:700}
  .coupon .big{color:var(--red);font-size:33px;line-height:30px;letter-spacing:1px}
  .coupon .small{font-size:9.5px;letter-spacing:.5px;line-height:10px}
  .coupon .note{font-weight:400;font-size:9px}
  .c1{left:43px;top:9px;width:126px;height:75px;padding-top:16px}
  .c2{left:169px;top:9px;width:129px;height:75px;padding-top:5px}
  .c3{left:43px;top:84px;width:126px;height:80px;padding-top:8px}
  .c2 .big{font-size:40px;line-height:36px}
  .c2 .big sup{font-size:20px;vertical-align:top;line-height:20px}
  .contact{position:absolute;left:175px;top:104px;width:150px;text-align:center;font-size:12px;line-height:13px;letter-spacing:.4px}
  .contact .phone{font-size:18.5px;margin-top:5px;line-height:20px}
  .back .brand{left:350px;top:48px;width:140px}
  .back .brand .name{font-size:14px;line-height:15px}
  .back .brand .tag{font-size:6px;margin-top:4px}
  .back .mail-address{position:absolute;left:336px;top:99px;width:168px;text-align:center;color:var(--ink);font-size:13px;line-height:13.5px}
  .mail-url{position:absolute;left:336px;top:145px;width:168px;text-align:center;color:var(--blue);font-size:13px;letter-spacing:.4px}
</style>
</head>
<body>

<section class="card front">
  <div class="hero-photo" role="img" aria-label="Photo of a house roof under construction with shingles and exposed gables"></div>
  <svg class="wave" width="674" height="505" viewBox="0 0 674 505">
    <path d="M0 220 L0 262 C90 268 190 290 300 318 C190 270 100 240 0 220 Z" fill="#1b1b1b"/>
    <path d="M0 262 C180 290 420 350 674 328 L674 468 L0 468 Z" fill="var(--blue)"/>
    <g stroke="#fff" stroke-width="5">
      <circle cx="289" cy="261" r="62" fill="#8fb6d6"/>
      <circle cx="549" cy="259" r="68" fill="#8a7a6c"/>
      <circle cx="414" cy="264" r="78" fill="#c9643f"/>
    </g>
    <title>Photos of roofers at work: on a roof, laying clay tiles, nailing shingles</title>
  </svg>

  <h1 class="headline">One Of The Most Trusted Roofing<br>Companies In Los Angeles</h1>

  <div class="brand">
    <div class="name">Kestrel Roofing Co.</div>
    <div class="tag">Since 1942<span class="sq"></span>State License 750419</div>
  </div>

  <div class="cta-label">CALL TODAY!</div>
  <div class="cta-phone">323-555-0174</div>
  <p class="address"><b>Kestrel Roofing Co. Inc</b><br>2287 W. Tamsin Street<br>Hollywood, Ca 90038</p>

  <ul class="credentials">
    <li><svg width="26" height="26" viewBox="0 0 26 26"><rect x="1" y="6" width="18" height="18" fill="none" stroke="#fff" stroke-width="2"/><path d="M5 14 L10 20 L24 2" fill="none" stroke="var(--green)" stroke-width="4"/></svg>LICENSED</li>
    <li><svg width="26" height="26" viewBox="0 0 26 26"><rect x="1" y="6" width="18" height="18" fill="none" stroke="#fff" stroke-width="2"/><path d="M5 14 L10 20 L24 2" fill="none" stroke="var(--green)" stroke-width="4"/></svg>BONDED</li>
    <li><svg width="26" height="26" viewBox="0 0 26 26"><rect x="1" y="6" width="18" height="18" fill="none" stroke="#fff" stroke-width="2"/><path d="M5 14 L10 20 L24 2" fill="none" stroke="var(--green)" stroke-width="4"/></svg>INSURED</li>
  </ul>

  <div class="partners" role="img" aria-label="Partner badges: LVR, Brackwold, Pellam Strude, Vantel Mark">
    <span style="background:var(--red)"></span>
    <span style="background:var(--blue-deep)"></span>
    <span style="background:#d9262b"></span>
    <span style="background:#3a8fd0"></span>
  </div>

  <div class="url-bar">www.Kestrelroofing.net</div>
</section>

<section class="card back">
  <div class="about">
    <p class="intro">We are a roofing company and we have been in Hollywood CA in the same location for over 90years</p>
    <h2 class="services-title">OUR SERVICES</h2>
    <h3 class="sectors">RESIDENTIAL, COMMERCIAL</h3>
    <ul class="services">
      <li><svg width="13" height="13" viewBox="0 0 13 13"><circle cx="6" cy="7" r="5" fill="none" stroke="#fff" stroke-width="1.2"/><path d="M3 7 L6 10 L12 1" fill="none" stroke="#fff" stroke-width="1.5"/></svg>Repairs</li>
      <li><svg width="13" height="13" viewBox="0 0 13 13"><circle cx="6" cy="7" r="5" fill="none" stroke="#fff" stroke-width="1.2"/><path d="M3 7 L6 10 L12 1" fill="none" stroke="#fff" stroke-width="1.5"/></svg>New Roofs</li>
      <li><svg width="13" height="13" viewBox="0 0 13 13"><circle cx="6" cy="7" r="5" fill="none" stroke="#fff" stroke-width="1.2"/><path d="M3 7 L6 10 L12 1" fill="none" stroke="#fff" stroke-width="1.5"/></svg>Energy Efficient</li>
      <li><svg width="13" height="13" viewBox="0 0 13 13"><circle cx="6" cy="7" r="5" fill="none" stroke="#fff" stroke-width="1.2"/><path d="M3 7 L6 10 L12 1" fill="none" stroke="#fff" stroke-width="1.5"/></svg>Cool Roofs Title 24</li>
      <li><svg width="13" height="13" viewBox="0 0 13 13"><circle cx="6" cy="7" r="5" fill="none" stroke="#fff" stroke-width="1.2"/><path d="M3 7 L6 10 L12 1" fill="none" stroke="#fff" stroke-width="1.5"/></svg>Skylights and More</li>
    </ul>
  </div>

  <div class="offers">
    <div class="coupon c1"><div class="big">FREE</div><div class="small">ROOF INSPECTION</div></div>
    <div class="coupon c2"><div class="big">10<sup>%</sup><span style="font-size:17px">OFF</span></div><div class="small" style="font-size:7.5px">NEW ROOF INSTALLATION</div><div class="note" style="margin-top:9px">Call For Details</div></div>
    <div class="coupon c3"><div class="big">FREE</div><div class="small">GUTTER CLEANING</div><div class="note" style="margin-top:4px;line-height:9px">WITH ANY<br>ROOF MAINTENANCE</div></div>
    <div class="contact">Contact Us For More Information<div class="phone">323-555-0174</div></div>
  </div>

  <div class="brand">
    <div class="name">Kestrel Roofing Co.</div>
    <div class="tag">Since 1942<span class="sq"></span>State License 750419</div>
  </div>
  <p class="mail-address"><b>Kestrel Roofing Co. Inc</b><br>2287 W. Tamsin Street<br>Hollywood, Ca 90038</p>
  <div class="mail-url">www.<b>Kestrelroofing</b>.net</div>
</section>

</body>
</html>
```